Below Par Parenting

I would like a poster (size to be agreed) created for the wording that I have composed and which I have pasted below. The poster is for my own personal gratification. It is not for commercial use. The message is driven by honesty and a profound sense of mea culpa. I am open to ideas regarding style and presentation.
I am an awful parent. No question. I am not cut out for this shit. I’m too quick to temper. I turn everything into a test of wills. I’m not down for food on the floor, for having my car trashed with your stink and detritus, for having the walls of my house daubed in your greasy fingerprints. I want to listen to The Marrows not Up the Paper Ladder on repeat. I enjoyed making you but, on reflection, I should have pulled out. Let me go back in time to that great waste of space and energy that is ante-natal classes and tell that boho with the flowery dress and curly hair, ‘Why are you concentrating on the first five seconds? All the pain comes later. Why aren’t you telling us what to do when they won’t sleep, when they won’t sit in their high chairs, when they won’t sleep on the aeroplane?’ Boy, I wish I could play it loosey-goosey like those left-leaning parents I see going ‘coo-coo’ in Benvolti’s but I’m not built like that. I am a right-wing despot. It’s Nazi Germany back at my place. I’m not interested in your meltdowns and tantrums. You want to writhe on the floor in the car park going red in the face? Make my day. You want to go spastic because I won’t let you watch TV for five hours straight? I don’t give a shit. Read my lips. I won’t pander to it. My wife says you’re babies but all I see is little people with an agenda. I’ve got naughty steps and sin-bins all over the joint. I wish I wasn’t the tyrant, the Valdarrez and the Okoro Tembe I am but it is what it is. I blame my parents and they, in turn, will blame me and their parents. Understand I don’t want to infect you too much with my bad behavior but if you could stop making such a scene in public places with your screaming, your bitching and your all round refusal to play nice then maybe, just maybe, we’d have a chance and I wouldn’t be such an awful parent.

```html
<!DOCTYPE html>
<html lang="en">
<head>
<meta charset="utf-8">
<title>Below Par Parenting</title>
<link rel="stylesheet" href="https://fonts.googleapis.com/css2?family=Arimo:ital,wght@0,400;0,700;1,400;1,700&display=swap">
<style>
  :root {
    --night: #000000;
    --chalk: #ffffff;
    --parchment-light: #f6e3a6;
    --parchment-mid: #e8c97f;
    --parchment-dark: #c99f55;
    --ink: #2b2516;
    --ink-block: #1d1a12;
    --ink-block-text: #f3dc9c;
  }
  * { margin: 0; padding: 0; box-sizing: border-box; }
  html, body {
    width: 1200px;
    height: 848px;
    overflow: hidden;
    background: var(--night);
  }
  .poster-spread {
    display: flex;
    width: 1200px;
    height: 848px;
  }
  .poster {
    position: relative;
    width: 600px;
    height: 848px;
    overflow: hidden;
  }
  .poster--night {
    background: var(--night);
    color: var(--chalk);
    --mark-bg: var(--chalk);
    --mark-fg: var(--night);
  }
  .poster--parchment {
    color: var(--ink);
    --mark-bg: var(--ink-block);
    --mark-fg: var(--ink-block-text);
  }
  .parchment-texture {
    position: absolute;
    inset: 0;
    background:
      radial-gradient(ellipse at 50% 45%, var(--parchment-light) 0%, var(--parchment-mid) 60%, var(--parchment-dark) 100%);
  }
  .confession {
    position: absolute;
    top: 63px;
    left: 52px;
    width: 497px;
    font-family: "Arimo", "Helvetica Neue", Arial, sans-serif;
    font-size: 17.2px;
    line-height: 23.9px;
    text-align: justify;
    text-align-last: left;
    letter-spacing: -0.1px;
  }
  .confession strong { font-weight: 700; }
  .confession em { font-style: italic; }
  .struck { text-decoration: line-through; text-decoration-thickness: 1px; }
  .mark {
    background: var(--mark-bg);
    color: var(--mark-fg);
    padding: 0 3px;
    -webkit-box-decoration-break: clone;
    box-decoration-break: clone;
  }
</style>
</head>
<body>
<main class="poster-spread">
  <section class="poster poster--night">
    <p class="confession">I am an awful parent. <strong>No question.</strong> I am not cut out for this <span class="struck">shit.</span> I’m too quick to temper. I turn everything into a test of wills. I’m not down for food on the floor, for having my car trashed with your stink and detritus, for having the walls of my house <em>daubed in your greasy fingerprints.</em> I want to listen to <span class="mark">The Marrows</span> not Up the Paper Ladder on repeat. I enjoyed making you but, on reflection, I should have pulled out. <em>Let me go back in time</em> to that great waste of space and energy that is ante-natal classes and tell that boho with the flowery dress and curly hair, <strong>‘Why are you concentrating on the first five seconds?</strong> <span class="mark">All the pain comes later.</span> Why aren’t you telling us what to do when they won’t sleep, when they won’t sit in their high chairs, when they won’t sleep on the aeroplane?’ Boy, I wish I could play it loosey-goosey like those left-leaning parents I see going ‘coo-coo’ in Benvolti’s but <span class="mark">I’m not built like that.</span> I am a right-wing despot. It’s <strong>Nazi Germany back at my place.</strong> I’m not interested in your meltdowns and tantrums. You want to writhe on the floor in the car park going red in the face? Make my day. <strong><em>You want to go spastic because I won’t let you watch TV for five hours straight?</em></strong> I don’t give a shit. Read my lips. I won’t pander to it. My wife says you’re babies but all I see is little people with an agenda. I’ve got naughty steps and sin-bins all over the joint. <span class="mark">I wish I wasn’t the tyrant,</span> the Valdarrez and the Okoro Tembe I am but it is what it is. I blame my parents and they, in turn, will blame me and their parents. Understand <span class="mark">I don’t want to infect you</span> too much with my bad behavior but if you could stop making such a scene in public places with your screaming, your bitching and your all round refusal to play nice then maybe, just maybe, we’d have a chance and <em>I wouldn’t be such an awful parent.</em></p>
  </section>

  <section class="poster poster--parchment">
    <div class="parchment-texture" role="img" aria-label="Aged, stained parchment paper texture in warm yellow and brown tones"></div>
    <p class="confession">I am an awful parent. <strong>No question.</strong> I am not cut out for this <span class="struck">shit.</span> I’m too quick to temper. I turn everything into a test of wills. I’m not down for food on the floor, for having my car trashed with your stink and detritus, for having the walls of my house <em>daubed in your greasy fingerprints.</em> I want to listen to <span class="mark">The Marrows</span> not Up the Paper Ladder on repeat. I enjoyed making you but, on reflection, I should have pulled out. <em>Let me go back in time</em> to that great waste of space and energy that is ante-natal classes and tell that boho with the flowery dress and curly hair, <strong>‘Why are you concentrating on the first five seconds?</strong> <span class="mark">All the pain comes later.</span> Why aren’t you telling us what to do when they won’t sleep, when they won’t sit in their high chairs, when they won’t sleep on the aeroplane?’ Boy, I wish I could play it loosey-goosey like those left-leaning parents I see going ‘coo-coo’ in Benvolti’s but <span class="mark">I’m not built like that.</span> I am a right-wing despot. It’s <strong>Nazi Germany back at my place.</strong> I’m not interested in your meltdowns and tantrums. You want to writhe on the floor in the car park going red in the face? Make my day. <strong><em>You want to go spastic because I won’t let you watch TV for five hours straight?</em></strong> I don’t give a shit. Read my lips. I won’t pander to it. My wife says you’re babies but all I see is little people with an agenda. I’ve got naughty steps and sin-bins all over the joint. <span class="mark">I wish I wasn’t the tyrant,</span> the Valdarrez and the Okoro Tembe I am but it is what it is. I blame my parents and they, in turn, will blame me and their parents. Understand <span class="mark">I don’t want to infect you</span> too much with my bad behavior but if you could stop making such a scene in public places with your screaming, your bitching and your all round refusal to play nice then maybe, just maybe, we’d have a chance and <em>I wouldn’t be such an awful parent.</em></p>
  </section>
</main>
</body>
</html>
```